New Facebook Banner

Hi
We are operating Ramen shop in Australia.(http://tsurumenoodle.net)
I want to create new design for our Facebook banner and title is "Free Ramen on your Birthday".
Sample attached is our existing banner design. We would like to make it more modern and sophisticated.
We are so looking forward to seeing your design for our free ramen promotion.

https://www.facebook.com/tsurumenoodle/

Industry/Entity Type

Japanese Restaurant

Font styles to use
Sans Serif

```html
<!DOCTYPE html>
<html lang="en">
<head>
<meta charset="utf-8">
<title>Free Ramen on Your Birthday – Cover Banners</title>
<link rel="stylesheet" href="https://fonts.googleapis.com/css2?family=Baloo+2:wght@800&display=swap">
<style>
  :root {
    --stage: #262626;
    --navy: #170b8c;
    --red: #f41010;
    --sun: #ffe400;
    --gold: #ffd21c;
    --orange: #ff7a00;
    --ink: #111111;
    --white: #ffffff;
    --party-pink: rgba(255, 60, 170, 0.35);
    --party-blue: rgba(60, 140, 255, 0.35);
    --party-yellow: rgba(255, 220, 0, 0.35);
    --party-green: rgba(60, 200, 90, 0.3);
  }
  * { box-sizing: border-box; margin: 0; padding: 0; }
  html, body {
    width: 1200px; height: 1200px; overflow: hidden;
    background: var(--stage);
  }
  .stage {
    position: relative; width: 1200px; height: 1200px;
    display: flex; flex-direction: column; align-items: center; justify-content: center; gap: 16px;
  }
  .banner {
    position: relative; width: 681px; height: 252px; overflow: hidden;
    background: var(--banner-bg);
  }
  .banner--navy { --banner-bg: var(--navy); --ramen-fill: #e5161b; --ramen-stroke: var(--sun); }
  .banner--red { --banner-bg: var(--red); --ramen-fill: var(--ink); --ramen-stroke: var(--sun); }
  .banner__sweep { position: absolute; inset: 0; width: 100%; height: 100%; }
  .banner__party {
    position: absolute; left: 170px; top: 0; width: 511px; height: 252px;
    background:
      radial-gradient(circle 60px at 60px 210px, var(--party-pink), transparent 100%),
      radial-gradient(circle 50px at 110px 40px, var(--party-yellow), transparent 100%),
      radial-gradient(circle 55px at 140px 130px, var(--party-blue), transparent 100%),
      radial-gradient(circle 55px at 330px 225px, var(--party-blue), transparent 100%),
      radial-gradient(circle 50px at 410px 60px, var(--party-pink), transparent 100%),
      radial-gradient(circle 45px at 260px 20px, var(--party-green), transparent 100%),
      radial-gradient(circle 45px at 420px 200px, var(--party-yellow), transparent 100%);
  }
  .banner__bowl {
    position: absolute; left: 13px; top: 9px; width: 232px; height: 232px; border-radius: 50%;
    background: radial-gradient(circle at 50% 50%, #c98c3c 0%, #8a5a25 55%, #3b3430 72%, #2a2624 100%);
  }
  .banner__balloons {
    position: absolute; right: 0; top: 0; width: 125px; height: 252px;
    border-radius: 70px 0 0 70px;
    background: linear-gradient(180deg, #e8c43a 0%, #9cbf3e 38%, #ff8a24 70%, rgba(255, 122, 0, 0) 100%);
    opacity: 0.92;
  }
  .headline {
    position: absolute; left: 298px; top: 24px; width: 264px;
    display: flex; flex-direction: column; align-items: center;
    font-family: "Baloo 2", sans-serif; font-weight: 800; line-height: 0.86;
    paint-order: stroke fill; letter-spacing: 0.5px;
  }
  .headline__free { font-size: 72px; color: var(--sun); -webkit-text-stroke: 6px var(--orange); }
  .headline__ramen { font-size: 50px; color: var(--ramen-fill); -webkit-text-stroke: 5px var(--ramen-stroke); }
  .headline__your { font-size: 46px; color: var(--sun); -webkit-text-stroke: 5px var(--orange); }
  .headline__birthday { font-size: 58px; color: var(--white); -webkit-text-stroke: 6px var(--gold); }
</style>
</head>
<body>
<main class="stage">

  <section class="banner banner--navy">
    <svg class="banner__sweep" viewBox="0 0 681 252" aria-hidden="true">
      <path d="M0 0 H205 C250 70 255 180 175 252 H0 Z" fill="var(--red)"/>
      <path d="M0 0 H185 C228 70 232 180 150 252 H0 Z" fill="var(--sun)"/>
    </svg>
    <div class="banner__party" role="img" aria-label="Scattered party confetti and curly streamers"></div>
    <div class="banner__bowl" role="img" aria-label="Photo of a bowl of chicken ramen with egg, spring onion and chopsticks"></div>
    <div class="banner__balloons" role="img" aria-label="Illustration of gold, green and orange party balloons"></div>
    <h1 class="headline">
      <span class="headline__free">FREE</span>
      <span class="headline__ramen">Ramen on</span>
      <span class="headline__your">Your</span>
      <span class="headline__birthday">Birthday</span>
    </h1>
  </section>

  <section class="banner banner--red">
    <svg class="banner__sweep" viewBox="0 0 681 252" aria-hidden="true">
      <path d="M0 0 H185 C228 70 232 180 150 252 H0 Z" fill="var(--sun)"/>
    </svg>
    <div class="banner__party" role="img" aria-label="Scattered party confetti and curly streamers"></div>
    <div class="banner__bowl" role="img" aria-label="Photo of a bowl of chicken ramen with egg, spring onion and chopsticks"></div>
    <div class="banner__balloons" role="img" aria-label="Illustration of gold, green and orange party balloons"></div>
    <h2 class="headline">
      <span class="headline__free">FREE</span>
      <span class="headline__ramen">Ramen on</span>
      <span class="headline__your">Your</span>
      <span class="headline__birthday">Birthday</span>
    </h2>
  </section>

</main>
</body>
</html>
```